Corevail health fitness personal training classes 8 week challenges

Corevail (aust) pty ltd is the business name I have only a Facebook page corevail Marla

I instruct 4 classes fitness classes a week and run 8 week challenges aprox 3-5 a year. I do personal training and write programs
These web sites are similar to what Iam looking for
Tess rowan 8 week program
Paula Venn
Roxanne finch

The above sites offer what I offer
Bonus is mine can be done online and in person which can be draining since I then take in a lot of emotional stuff and stories and excuses from clients

They get given training programs which is what I do written programs but I also give them physical training sessions as well

The purpose of this site?
My goal is to stay in the health and fitness industry however my body is physically, emotionally mentally exhausted.
I am torn because I love my job but 28 years later and with a few health issues I can't do it.
I must stop i need to stop due to
My health but I can't I worry about the loss of income and letting people down

So if I can set up a website and a online app, 8 week challenge or add to my collection of fitness DVDs and put them online where I can work from home

on my Facebook you can access my albums and advertising material

My main primary audience is females between 25-55 however I cater for everyone young old for unfit challenged etc

On my website or app these are the things I would want to cover

Everyday there would be a new inspirational logo
A short program they can do in the privacy of there home
My fitness DVD's and workout clothing on sale
Fitness programs on sale

I have an in in inbundance of information I can draw from of eg my 3 fitness DVDs, receipes, logos, inspirational quotes from my Facebook so stuff I have used before I am wanting to produce another DVD And complete my book I would love to add that to my products

Eye catching words
Weight loss (only because that gets people in straight away)
Fat burner (example I teach a abs thigh butt class Monday yes it's burns calories as much as the Fatburner class but uneducated people will go to the Fatburner just because of the name

Corevail

28 years experience ( I believe i have so much experience and stories to share I have the qualifications and awards that I have won but it's my passion and desire to help others I think this is why my business is a success.
Can this translate online ??

I have won fitness professional awards

I want people to connect with me and I want there first reaction to be of hope and courage and know that they can do this that real wow anything is possible
Corevail is about the member and I genuinely care Yhey are not just a number

​I want them to trust that I have the knowledge and experience
Online fitness programs
The selling of my fitness DVDs
Online 8 week programs
Recipes
Before and after photos
Client testimonials

Target Market(s)

Majority a females aged between 18-60 years old

Industry/Entity Type

Health And Wellness

Coding

Coded - Design and coding required

Number of Pages Required

1 page

Font styles to use
Serif
Script

Colors
f37122
faa54b
3c7bb8
33a6d7

Requirements
Must have
• Albums / files as below
• Client testimonials
• Before and after photos
• Selling products eg DVD's/ programs etc
Nice to have
• My aim is to take my business more into online so I can still offer all my services eg classes, programs, nutritional advice, one on one consultant,
• However have the bonus of doing it from home online.
• Also my body needs to physically slow down
Should not have
• Not sure on this question

```html
<!DOCTYPE html>
<html lang="en">
<head>
<meta charset="utf-8">
<title>Corevail — Health, Fitness &amp; 8 Week Challenges</title>
<link rel="stylesheet" href="https://fonts.googleapis.com/css2?family=Roboto:wght@400;500;700&family=Open+Sans:wght@400;600&display=swap">
<style>
:root{
  --orange:#f37122;
  --orange-soft:#faa54b;
  --blue:#3c7bb8;
  --sky:#33a6d7;
  --blue-band:#3a8fd0;
  --ink:#333;
  --muted:#666;
  --line:#ddd;
  --header-bg:#dfe5ef;
  --grey-bg:#f2f2f2;
  --footer-bg:#232323;
  --white:#fff;
}
*{box-sizing:border-box;margin:0;padding:0}
html,body{width:1200px;height:3659px;overflow:hidden}
body{font-family:"Open Sans",Arial,sans-serif;color:var(--ink);background:var(--white);position:relative}
section,header,footer,nav{position:absolute;left:0;width:1200px}

/* header */
.site-header{top:0;height:90px;background:var(--header-bg);display:flex;align-items:center;justify-content:center}
.brand{font-family:"Roboto",sans-serif;font-weight:700;font-size:34px;letter-spacing:1px;color:var(--blue);display:flex;align-items:center;gap:10px}
.brand-dot{width:16px;height:16px;border-radius:50%;background:var(--orange)}
.main-nav{top:90px;height:61px;background:var(--orange);display:flex;justify-content:center;align-items:center;gap:33px}
.main-nav a{font-family:"Roboto",sans-serif;font-weight:500;font-size:12.5px;color:var(--white);text-decoration:none;text-transform:uppercase}

/* hero */
.hero{top:151px;height:525px;color:var(--white);text-align:center;
  background:
    radial-gradient(ellipse 40% 30% at 20% 30%,rgba(120,110,100,.45),transparent 70%),
    radial-gradient(ellipse 35% 30% at 80% 25%,rgba(110,105,100,.4),transparent 70%),
    radial-gradient(ellipse 60% 30% at 50% 85%,rgba(90,80,70,.45),transparent 70%),
    linear-gradient(180deg,#3b3936 0%,#262422 55%,#302d2a 100%)}
.hero::after{content:"";position:absolute;inset:0;background:rgba(0,0,0,.25)}
.hero > *{z-index:1}
.hero-title{position:absolute;top:145px;width:100%;font-family:"Roboto",sans-serif;font-weight:500;font-size:54px;letter-spacing:2px}
.hero-text{position:absolute;top:226px;left:235px;width:730px;font-size:14.5px;line-height:30px;color:#e6e6e6}
.hero-btn{position:absolute;top:316px;left:485px;width:230px;height:44px;border:1px solid #fff;font-family:"Roboto",sans-serif;font-size:12px;line-height:42px;text-transform:uppercase;letter-spacing:.5px}
.hero-dots{position:absolute;top:481px;left:0;width:100%;display:flex;justify-content:center;gap:6px}
.hero-dots span{width:13px;height:13px;border-radius:50%;border:2px solid #fff}
.hero-dots span.active{background:var(--orange);border-color:var(--orange)}

/* headings */
.section-title{font-family:"Roboto",sans-serif;font-weight:700;font-size:22px;color:var(--orange);text-transform:uppercase}
.section-sub{font-size:13px;color:var(--muted)}
.center{text-align:center;width:100%;position:absolute;left:0}

/* online programs */
.programs{top:676px;height:414px}
.programs .section-title{position:absolute;left:86px;top:46px}
.programs-copy{position:absolute;left:88px;top:90px;width:480px;font-size:12.5px;line-height:25px;color:var(--muted)}
.programs-copy p+p{margin-top:14px}
.btn-orange{position:absolute;background:var(--orange);color:var(--white);font-family:"Roboto",sans-serif;font-weight:500;font-size:13px;text-transform:uppercase;text-align:center}
.programs .btn-orange{left:88px;top:334px;width:150px;height:40px;line-height:40px}
.video-frame{position:absolute;left:612px;top:51px;width:500px;height:312px;
  background:
    radial-gradient(ellipse 30% 40% at 70% 35%,rgba(220,200,180,.55),transparent 70%),
    radial-gradient(ellipse 35% 40% at 25% 55%,rgba(235,230,220,.55),transparent 70%),
    linear-gradient(135deg,#5d5a58,#3a3836 60%,#262524)}
.play{position:absolute;left:210px;top:116px}

/* products */
.products{top:1090px;height:512px;background:var(--grey-bg)}
.products .section-title{top:35px}
.products .section-sub{top:70px}
.product-card{position:absolute;top:122px;width:234px;height:342px;background:var(--white);border:1px solid #e6e6e6;text-align:center}
.product-img{position:absolute;left:14px;top:14px;right:14px;height:174px;border:1px solid #eee}
.product-price{position:absolute;top:210px;width:100%;font-family:"Roboto",sans-serif;font-size:21px;color:var(--orange)}
.product-name{position:absolute;top:250px;width:100%;font-family:"Roboto",sans-serif;font-weight:500;font-size:14px;color:#444;text-transform:uppercase}
.product-actions{position:absolute;top:284px;width:100%;display:flex;justify-content:center;gap:8px}
.product-actions span{width:30px;height:30px;border-radius:50%;border:1px solid #ccc;display:flex;align-items:center;justify-content:center}
.product-actions span.cart{background:#888;border-color:#888}

/* free trial */
.trial{top:1602px;height:720px;
  background:
    radial-gradient(ellipse 50% 25% at 30% 80%,rgba(150,150,150,.5),transparent 70%),
    linear-gradient(180deg,#4a4a4a,#6d6d6d 55%,#8a8a8a)}
.trial-card{position:absolute;left:339px;top:47px;width:522px;height:613px;background:var(--white)}
.trial-img{position:absolute;left:0;top:0;width:522px;height:273px;
  background:
    radial-gradient(ellipse 60% 30% at 50% 70%,rgba(150,120,110,.55),transparent 70%),
    radial-gradient(ellipse 40% 20% at 50% 10%,rgba(200,200,220,.35),transparent 70%),
    linear-gradient(180deg,#1e1e24,#3c3a42 60%,#2a292e)}
.trial-card .section-title{position:absolute;left:29px;top:297px;font-size:21px}
.trial-text{position:absolute;left:29px;top:334px;width:470px;font-size:12.5px;line-height:24px;color:var(--muted)}
.field{position:absolute;left:29px;width:464px;height:40px;border:1px solid #ccc;border-radius:3px;font-size:12px;color:#777;padding-left:12px;line-height:38px}
.trial .btn-orange{left:29px;top:551px;width:122px;height:37px;line-height:37px}

/* before after */
.results{top:2322px;height:563px;background:var(--blue-band);color:var(--white)}
.results .section-title{top:48px;color:var(--white)}
.results .section-sub{top:82px;color:#e8f1fa}
.result-card{position:absolute;top:127px;width:322px;height:371px;background:var(--white);color:var(--ink)}
.result-photo{position:absolute;left:0;top:0;width:322px;height:209px;display:flex;gap:3px;background:#fff}
.result-photo div{flex:1}
.badge{position:absolute;left:9px;top:168px;width:76px;height:76px;border-radius:50%;background:var(--blue);color:var(--white);text-align:center;font-family:"Roboto",sans-serif;border:3px solid #fff}
.badge small{display:block;font-size:11px;margin-top:15px}
.badge strong{font-size:22px}
.badge strong i{font-style:normal;font-size:13px}
.result-name{position:absolute;right:40px;top:230px;font-family:"Roboto",sans-serif;font-weight:500;font-size:18px;color:#444;text-transform:uppercase}
.result-quote{position:absolute;left:26px;top:272px;width:270px;text-align:center;font-size:12px;line-height:25px;color:var(--muted)}
.qm{font-family:Georgia,serif;font-size:26px;color:#444;line-height:0;position:relative;top:8px}

/* blog */
.blog{top:2885px;height:537px}
.blog .section-title{top:35px}
.blog .section-sub{top:67px}
.post{position:absolute;top:115px;width:326px}
.post-img{height:205px}
.post-title{margin-top:28px;font-family:"Roboto",sans-serif;font-weight:700;font-size:14px;color:#444;text-transform:uppercase}
.post-meta{margin-top:14px;padding:6px 0;border-top:1px solid var(--line);border-bottom:1px solid var(--line);display:flex;justify-content:space-between;font-size:9.5px;color:#888}
.post-text{margin-top:14px;font-size:12px;line-height:27px;color:var(--muted)}

/* footer */
.site-footer{top:3422px;height:237px;background:var(--footer-bg);color:#ddd}
.social{position:absolute;top:29px;left:0;width:100%;display:flex;justify-content:center;gap:9px}
.social span{width:64px;height:64px;border-radius:50%;border:1px solid #999;display:flex;align-items:center;justify-content:center}
.social i{width:12px;height:12px;border-radius:50%;background:#fff}
.footer-nav{position:absolute;top:130px;width:100%;display:flex;justify-content:center;font-family:"Roboto",sans-serif;font-size:12px;text-transform:uppercase}
.footer-nav a{color:#ddd;text-decoration:none;padding:0 14px;border-right:1px solid #888}
.footer-nav a:last-child{border:none}
.copyright{position:absolute;top:172px;width:100%;text-align:center;font-size:12px;color:#ccc}
</style>
</head>
<body>

<header class="site-header">
  <div class="brand"><span class="brand-dot"></span>COREVAIL</div>
</header>

<nav class="main-nav">
  <a>Home</a><a>Online Fitness Programs</a><a>Fitness DVDs</a><a>Online 8 Week Programs</a><a>Recipes</a><a>Before &amp;After Photos</a><a>Client Testimonials</a><a>Contact</a>
</nav>

<section class="hero" role="img" aria-label="Group fitness class in a gym, dark photo backdrop">
  <h1 class="hero-title">COREVAIL</h1>
  <p class="hero-text">Sed ut perspiciatis unde omnis iste natus error sit voluptatem accusantium doloremque laudantium, totam ipsa quae ab illo inventore veritatis et quasi architecto beatae vitae dicta sunt explicabo.</p>
  <div class="hero-btn">Click here for more info</div>
  <div class="hero-dots"><span></span><span></span><span class="active"></span><span></span><span></span></div>
</section>

<section class="programs">
  <h2 class="section-title">Online Fitness Programs</h2>
  <div class="programs-copy">
    <p>Sed ut perspiciatis unde omnis iste natus error sit voluptatem accusantium dolorem que laudantium, totam rem aperiam, eaque ipsa quae ab illo inventore veritatis et qu asi architecto beatae vitae dicta sunt explicabo. Nemo enim ipsam voluptatem quia voluptas sit aspernatur aut odit aut fugit, sed quia consequuntur magni dolores eos qui ratione voluptatem sequi nesciunt.</p>
    <p>Eaque ipsa quae ab illo inventore veritatis et qu asi architecto beatae vitae dicta sunt explicabo. Nemo enim ipsam voluptatem quia voluptas sit aspernatur aut odit aut fugi ni dolores eos qui ratione voluptatem sequi nesciunt.</p>
  </div>
  <div class="btn-orange">Watch Video</div>
  <div class="video-frame" role="img" aria-label="Video still of the trainer holding a fitness award certificate">
    <svg class="play" width="80" height="80" viewBox="0 0 80 80"><circle cx="40" cy="40" r="37" fill="rgba(0,0,0,.35)" stroke="#fff" stroke-width="3"/><path d="M32 25 L56 40 L32 55Z" fill="#fff"/></svg>
  </div>
</section>

<section class="products">
  <h2 class="section-title center">Featured Products</h2>
  <p class="section-sub center">Sed ut perspiciatis unde omnis iste natus error sit voluptatem accusantium dolorem que laudantium,</p>

  <div class="product-card" style="left:88px">
    <div class="product-img" role="img" aria-label="Lime green workout singlet" style="background:radial-gradient(ellipse 45% 55% at 50% 50%,#c6e84a,#e4f2b0 60%,#f7f7f7 100%)"></div>
    <div class="product-price">$ 5.99</div><div class="product-name">Workout Clothing</div>
    <div class="product-actions">
      <span class="cart"><svg width="14" height="14" viewBox="0 0 14 14"><path d="M1 2h2l2 7h6l2-5H4" fill="none" stroke="#fff" stroke-width="1.4"/><circle cx="6" cy="12" r="1.2" fill="#fff"/><circle cx="10" cy="12" r="1.2" fill="#fff"/></svg></span>
      <span><svg width="14" height="13" viewBox="0 0 14 13"><path d="M7 12 L1.5 6.5 A3 3 0 0 1 7 2.5 A3 3 0 0 1 12.5 6.5Z" fill="none" stroke="#888" stroke-width="1.3"/></svg></span>
      <span><svg width="14" height="12" viewBox="0 0 14 12"><path d="M1 3h11M9 0.5l3 2.5-3 2.5M13 9H2M5 6.5l-3 2.5 3 2.5" fill="none" stroke="#888" stroke-width="1.3"/></svg></span>
    </div>
  </div>
  <div class="product-card" style="left:349px">
    <div class="product-img" role="img" aria-label="Fitness DVD case with disc" style="background:radial-gradient(ellipse 45% 55% at 50% 50%,#cfcfcf,#e6e6e6 60%,#f7f7f7 100%)"></div>
    <div class="product-price">$ 5.99</div><div class="product-name">Workout DVDs</div>
    <div class="product-actions">
      <span class="cart"><svg width="14" height="14" viewBox="0 0 14 14"><path d="M1 2h2l2 7h6l2-5H4" fill="none" stroke="#fff" stroke-width="1.4"/><circle cx="6" cy="12" r="1.2" fill="#fff"/><circle cx="10" cy="12" r="1.2" fill="#fff"/></svg></span>
      <span><svg width="14" height="13" viewBox="0 0 14 13"><path d="M7 12 L1.5 6.5 A3 3 0 0 1 7 2.5 A3 3 0 0 1 12.5 6.5Z" fill="none" stroke="#888" stroke-width="1.3"/></svg></span>
      <span><svg width="14" height="12" viewBox="0 0 14 12"><path d="M1 3h11M9 0.5l3 2.5-3 2.5M13 9H2M5 6.5l-3 2.5 3 2.5" fill="none" stroke="#888" stroke-width="1.3"/></svg></span>
    </div>
  </div>
  <div class="product-card" style="left:610px">
    <div class="product-img" role="img" aria-label="Black workout top and shorts" style="background:radial-gradient(ellipse 40% 55% at 50% 50%,#2e3036,#8a8c92 60%,#f7f7f7 100%)"></div>
    <div class="product-price">$ 5.99</div><div class="product-name">Workout Clothing</div>
    <div class="product-actions">
      <span class="cart"><svg width="14" height="14" viewBox="0 0 14 14"><path d="M1 2h2l2 7h6l2-5H4" fill="none" stroke="#fff" stroke-width="1.4"/><circle cx="6" cy="12" r="1.2" fill="#fff"/><circle cx="10" cy="12" r="1.2" fill="#fff"/></svg></span>
      <span><svg width="14" height="13" viewBox="0 0 14 13"><path d="M7 12 L1.5 6.5 A3 3 0 0 1 7 2.5 A3 3 0 0 1 12.5 6.5Z" fill="none" stroke="#888" stroke-width="1.3"/></svg></span>
      <span><svg width="14" height="12" viewBox="0 0 14 12"><path d="M1 3h11M9 0.5l3 2.5-3 2.5M13 9H2M5 6.5l-3 2.5 3 2.5" fill="none" stroke="#888" stroke-width="1.3"/></svg></span>
    </div>
  </div>
  <div class="product-card" style="left:871px">
    <div class="product-img" role="img" aria-label="Black fitness DVD case" style="background:radial-gradient(ellipse 40% 55% at 50% 50%,#333,#8f8f8f 60%,#f7f7f7 100%)"></div>
    <div class="product-price">$ 5.99</div><div class="product-name">Workout DVDs</div>
    <div class="product-actions">
      <span class="cart"><svg width="14" height="14" viewBox="0 0 14 14"><path d="M1 2h2l2 7h6l2-5H4" fill="none" stroke="#fff" stroke-width="1.4"/><circle cx="6" cy="12" r="1.2" fill="#fff"/><circle cx="10" cy="12" r="1.2" fill="#fff"/></svg></span>
      <span><svg width="14" height="13" viewBox="0 0 14 13"><path d="M7 12 L1.5 6.5 A3 3 0 0 1 7 2.5 A3 3 0 0 1 12.5 6.5Z" fill="none" stroke="#888" stroke-width="1.3"/></svg></span>
      <span><svg width="14" height="12" viewBox="0 0 14 12"><path d="M1 3h11M9 0.5l3 2.5-3 2.5M13 9H2M5 6.5l-3 2.5 3 2.5" fill="none" stroke="#888" stroke-width="1.3"/></svg></span>
    </div>
  </div>
</section>

<section class="trial" role="img" aria-label="Greyscale background photo of a fitness class">
  <div class="trial-card">
    <div class="trial-img" role="img" aria-label="Large fitness class exercising under stage lights"></div>
    <h2 class="section-title">Free Trial</h2>
    <p class="trial-text">Sed ut perspiciatis unde omnis iste natus error sit voluptatem accusantium veritatis et quasi architecto beatae vitae dicta sunt explicabo.</p>
    <div class="field" style="top:396px">First Name :</div>
    <div class="field" style="top:445px">Last Name :</div>
    <div class="field" style="top:494px">Email :</div>
    <div class="btn-orange">Submit</div>
  </div>
</section>

<section class="results">
  <h2 class="section-title center">Before &amp; After Photos</h2>
  <p class="section-sub center">Sed ut perspiciatis unde omnis iste natus error sit voluptatem accusantium dolorem que laudantium,</p>

  <div class="result-card" style="left:88px">
    <div class="result-photo" role="img" aria-label="Before and after body transformation photos"><div style="background:linear-gradient(180deg,#e0b49a,#c48f72 55%,#6e5a4e)"></div><div style="background:linear-gradient(180deg,#d8aa8e,#b88468 55%,#6a5648)"></div></div>
    <div class="badge"><small>LOST</small><strong>6<i>KG</i></strong></div>
    <div class="result-name">Jhon Smith</div>
    <p class="result-quote"><span class="qm">&ldquo;</span> Sed ut perspiciatis unde omnis iste natus error sit voluptatem accusantium doloremque lau be atae vitae dicta sunt explicabo. <span class="qm">&rdquo;</span></p>
  </div>
  <div class="result-card" style="left:439px">
    <div class="result-photo" role="img" aria-label="Before and after side profile photos"><div style="background:linear-gradient(180deg,#e4d8cc,#c99c80 50%,#8a6a58)"></div><div style="background:linear-gradient(180deg,#d9c9bb,#bf8e72 50%,#7d5f4e)"></div></div>
    <div class="badge"><small>LOST</small><strong>6<i>KG</i></strong></div>
    <div class="result-name">Jhon Smith</div>
    <p class="result-quote"><span class="qm">&ldquo;</span> Sed ut perspiciatis unde omnis iste natus error sit voluptatem accusantium doloremque lau be atae vitae dicta sunt explicabo. <span class="qm">&rdquo;</span></p>
  </div>
  <div class="result-card" style="left:790px">
    <div class="result-photo" role="img" aria-label="Before and after transformation photos in sports wear"><div style="background:linear-gradient(180deg,#d6b39c,#3f5a86 45%,#2f3f5c)"></div><div style="background:linear-gradient(180deg,#cda58c,#2a2a2e 50%,#3a3032)"></div></div>
    <div class="badge"><small>LOST</small><strong>6<i>KG</i></strong></div>
    <div class="result-name">Jhon Smith</div>
    <p class="result-quote"><span class="qm">&ldquo;</span> Sed ut perspiciatis unde omnis iste natus error sit voluptatem accusantium doloremque lau be atae vitae dicta sunt explicabo. <span class="qm">&rdquo;</span></p>
  </div>
</section>

<section class="blog">
  <h2 class="section-title center">Latest Blog</h2>
  <p class="section-sub center">Sed ut perspiciatis unde omnis iste natus error sit voluptatem accusantium dolorem que laudantium</p>

  <article class="post" style="left:88px">
    <div class="post-img" role="img" aria-label="Women training with dumbbells in a gym" style="background:radial-gradient(ellipse 40% 45% at 35% 55%,#e7c2a8,transparent 70%),radial-gradient(ellipse 30% 40% at 75% 40%,#c8e04a,transparent 70%),linear-gradient(135deg,#d9cbbb,#8e7b6c)"></div>
    <h3 class="post-title">Contrary to popular</h3>
    <div class="post-meta"><span>27 MARCH 2017</span><span>120</span><span>LIKE</span><span>SHARE</span></div>
    <p class="post-text">Sed ut perspiciatis unde omnis iste natus error sit volupta tem accusantium doloremque laudantium, totam rem arch itecto beatae vitae dicta sunt explicabo.</p>
  </article>
  <article class="post" style="left:437px">
    <div class="post-img" role="img" aria-label="Step aerobics class" style="background:radial-gradient(ellipse 50% 35% at 50% 45%,#d8758f,transparent 70%),radial-gradient(ellipse 60% 20% at 50% 88%,#3b3f5a,transparent 70%),linear-gradient(135deg,#b59aa8,#5c4a6a)"></div>
    <h3 class="post-title">Contrary to popular</h3>
    <div class="post-meta"><span>27 MARCH 2017</span><span>120</span><span>LIKE</span><span>SHARE</span></div>
    <p class="post-text">Sed ut perspiciatis unde omnis iste natus error sit volupta tem accusantium doloremque laudantium, totam rem arch itecto beatae vitae dicta sunt explicabo.</p>
  </article>
  <article class="post" style="left:786px">
    <div class="post-img" role="img" aria-label="Woman doing a plank with a medicine ball" style="background:radial-gradient(circle at 78% 72%,#e0a23a 0 12%,transparent 14%),radial-gradient(ellipse 45% 25% at 45% 60%,#7a5440,transparent 70%),linear-gradient(135deg,#a88466,#4a3a30)"></div>
    <h3 class="post-title">Contrary to popular</h3>
    <div class="post-meta"><span>27 MARCH 2017</span><span>120</span><span>LIKE</span><span>SHARE</span></div>
    <p class="post-text">Sed ut perspiciatis unde omnis iste natus error sit volupta tem accusantium doloremque laudantium, totam rem arch itecto beatae vitae dicta sunt explicabo.</p>
  </article>
</section>

<footer class="site-footer">
  <div class="social">
    <span><i></i></span><span><i></i></span><span><i></i></span><span><i></i></span><span><i></i></span>
    <span><svg width="22" height="16" viewBox="0 0 22 16"><rect x="1" y="1" width="20" height="14" fill="none" stroke="#fff" stroke-width="1.6"/><path d="M1 1 L11 9 L21 1" fill="none" stroke="#fff" stroke-width="1.6"/></svg></span>
  </div>
  <nav class="footer-nav">
    <a>Home</a><a>Online Fitness Programs</a><a>Fitness DVDs</a><a>Online 8 Week Programs</a><a>Recipes</a><a>Before &amp; After Photos</a><a>Client Testimonials</a><a>Contact</a>
  </nav>
  <p class="copyright">© Copyrights 2017 Corevail.All Rights Reserved.</p>
</footer>

</body>
</html>
```